Cardiology Practice needs a Heart Scan Order Form

Busy cardiology practice needs an order form for a heart scan test. Sample is attached. One side should have all information noted and the other side should have our physician names (Dorian Velko, MD, L.N. Morvesti, MD, Ovila Brandt, MD, Tomas Velko, MD, and Gerald Pompetti, MD. It should have the map that is uploaded and our demographic information (Crestfield Cardiac PLLC, 712 Harrow Ln. Ste. K, Melrick, TX 77431 along with phone 832-417-2286 and fax 832-417-2287) as well as our web address (crestfieldcardiac.example). Our primary colors are red, black and white. Needs to fit paper size 8 1/2 by 11.

Target Market(s)

Healthcare

Industry/Entity Type

Health Care

Font styles to use
Serif

Colors
ec1f27

Requirements
Must have
• Logo, information listed on sample form, demographics and physician names as well as website.
Nice to have
• Open to suggestions
Should not have
• Physician Pictures

```html
<!DOCTYPE html>
<html lang="en">
<head>
<meta charset="utf-8">
<title>Crestfield Cardiac – Calcium Score Heart Scan Order Form</title>
<link rel="stylesheet" href="https://fonts.googleapis.com/css2?family=Lato:ital,wght@0,300;0,400;0,700;0,900;1,400;1,700&display=swap">
<style>
:root{
  --red:#c81e2d;
  --black:#0c0c0c;
  --white:#ffffff;
  --grey-bar:#8b8b8b;
  --panel:#efefef;
  --line:#9a9a9a;
  --ink:#1a1a1a;
  --backdrop:#d6d6d6;
}
*{box-sizing:border-box;margin:0;padding:0}
html,body{width:1200px;height:1200px;overflow:hidden}
body{background:var(--backdrop);font-family:'Lato',sans-serif;color:var(--ink);position:relative}
.page{position:absolute;width:555px;height:716px;background:var(--white);overflow:hidden}
.page--form{left:31px;top:220px}
.page--info{left:617px;top:219px}
.abs{position:absolute}
.header-art{position:absolute;left:0;top:0}
.brand{position:absolute;display:flex;align-items:center;gap:8px;color:var(--red);font-weight:900;line-height:1.05}
.brand__dot{width:12px;height:12px;border-radius:50%;background:var(--red);flex:none}
.title{position:absolute;right:20px;color:var(--white);text-align:right;line-height:1}
.title__top{font-weight:300;display:block}
.title__main{font-weight:900;display:block}
.name-strip{position:absolute;left:0;width:100%;display:flex;justify-content:center;align-items:center;white-space:nowrap}
.name-strip .sep{color:var(--red);margin:0 6px;font-weight:700}
/* form page */
.doctors{top:73px;height:23px;background:var(--grey-bar);color:var(--white);font-size:10.5px}
.schedule{top:114px;left:14px;display:flex;align-items:center;font-size:10.5px;font-weight:700;gap:8px}
.schedule .red{color:var(--red)}
.box{border:1px solid var(--red);border-radius:2px;font-weight:400;padding:2px 10px;font-size:10px}
.section-bar{position:absolute;height:19px;color:var(--white);font-weight:700;font-size:12.5px;text-align:center;line-height:19px}
.section-bar--black{background:var(--black)}
.section-bar--red{background:var(--red)}
.fields{position:absolute;top:167px;font-size:9.5px;font-weight:700}
.fields .row{display:flex;align-items:flex-end;height:13px}
.fields .label{width:80px}
.fields .fill{flex:1;border-bottom:1px dotted var(--line);height:9px}
.med-panel{position:absolute;left:0;top:246px;width:100%;height:155px;background:var(--panel)}
.med-row{position:absolute;top:8px;left:13px;right:17px;display:flex;align-items:center;font-size:10px;font-weight:700}
.med-row .in{border:1px solid var(--red);border-radius:2px;height:19px;background:var(--white);font-weight:400;font-size:10px;display:flex;align-items:center;justify-content:center}
.diag-head{position:absolute;top:40px;left:13px;right:17px;display:flex;align-items:flex-end;font-size:10px;font-weight:700}
.diag-head .fill{flex:1;border-bottom:1px dotted var(--line);margin-left:4px;height:8px}
.check-col{position:absolute;top:59px;font-size:9.5px}
.check-col li{list-style:none;display:flex;align-items:center;height:17.5px}
.check-col li::before{content:"";width:15px;height:14px;border:1px solid var(--red);border-radius:2px;background:var(--white);margin-right:10px;flex:none}
.notice{position:absolute;top:405px;left:13px;font-size:9.3px;font-style:italic;font-weight:700;display:flex;align-items:center;gap:5px}
.notice__icon{width:12px;height:12px;border-radius:50%;background:var(--red);color:var(--white);font-size:9px;font-style:normal;text-align:center;line-height:12px}
.instructions{position:absolute;top:430px;left:14px;width:523px;height:143px;border:1px solid var(--red);padding:8px 14px 0 17px;font-size:8.9px;line-height:12.6px}
.instructions li{list-style:none;padding-left:11px;position:relative}
.instructions li::before{content:"";position:absolute;left:0;top:3px;width:7px;height:7px;border:1px solid var(--red)}
.instructions li.tick::after{content:"";position:absolute;left:2px;top:4px;width:3px;height:4px;border-right:1px solid var(--red);border-bottom:1px solid var(--red);transform:rotate(40deg)}
.instructions b{color:var(--red)}
.ack{position:absolute;top:581px;left:0;width:100%;text-align:center;font-size:9.2px;font-style:italic;font-weight:700;line-height:12.5px}
.sign{position:absolute;width:120px;border-top:1px solid var(--line);font-size:9px;font-weight:700;padding-top:2px}
.referral{position:absolute;left:284px;top:613px;width:254px;border:1px solid var(--red)}
.referral__head{background:var(--red);color:var(--white);font-size:9px;font-weight:700;height:21px;line-height:21px;padding-left:20px}
.referral__row{display:flex;height:21px;border-top:1px solid var(--red);font-size:9px;font-weight:700}
.referral__row span{width:116px;background:var(--panel);line-height:20px;padding-left:20px}
.foot-bar{position:absolute;left:0;bottom:0;width:100%;height:8px;background:var(--red)}
/* info page */
.photo{position:absolute;left:0;top:128px;width:100%;height:303px;background:linear-gradient(120deg,#c9d0d6 0%,#eef0f1 45%,#f4efe3 70%,#d9dde0 100%)}
.band{position:absolute;left:0;width:100%;text-align:center}
.band--red{background:var(--red);color:var(--white);font-weight:700;font-size:11px}
.band--names{font-size:10.8px}
.contact-zone{position:absolute;left:0;top:526px;width:100%;height:190px}
.contact-text{position:absolute;color:var(--white)}
.contact-lead{left:280px;top:22px;font-size:11px;font-weight:700}
.contact-block{left:356px;top:54px;font-size:11.3px;line-height:14.5px;font-weight:400}
.contact-block .co{font-weight:700}
.contact-line{display:flex;align-items:center;gap:7px}
.web{right:18px;top:156px;font-size:16px;font-weight:700;display:flex;align-items:center;gap:7px;white-space:nowrap}
</style>
</head>
<body>

<!-- ORDER FORM SIDE -->
<section class="page page--form" aria-label="Order form">
  <svg class="header-art" width="555" height="73" viewBox="0 0 555 73">
    <polygon points="236,73 246,73 286,0 276,0" fill="#c81e2d"/>
    <polygon points="256,73 555,73 555,0 296,0" fill="#c81e2d"/>
  </svg>
  <div class="brand" style="left:36px;top:28px;font-size:17px"><span class="brand__dot"></span>CRESTFIELD CARDIAC</div>
  <div class="title" style="top:12px"><span class="title__top" style="font-size:25px">CALCIUM SCORE</span><span class="title__main" style="font-size:32px;margin-top:2px">HEART SCAN</span></div>

  <div class="name-strip doctors">
    Dorian Velko, MD<span class="sep">|</span>L.N. Morvesti, MD<span class="sep">|</span>Ovila Brandt, MD<span class="sep">|</span>Tomas Velko, MD<span class="sep">|</span>Gerald Pompetti, MD
  </div>

  <div class="schedule abs">
    <span class="red">TEST SCHEDULE</span><span style="margin-left:4px">DATE:</span>
    <span class="box" style="padding:2px 12px">DD / &nbsp;MM / YYYY</span>
    <span style="margin-left:14px">TIME:</span><span class="box" style="padding:2px 8px">00:00</span>
  </div>

  <div class="section-bar section-bar--black" style="left:13px;top:137px;width:251px">PATIENT INFORMATION</div>
  <div class="section-bar section-bar--black" style="left:284px;top:137px;width:251px">CONTACT INFORMATION</div>

  <div class="fields" style="left:14px;width:250px">
    <div class="row"><span class="label">FIRST NAME</span><span class="fill"></span><span style="margin:0 8px 0 6px">MI</span><span class="fill" style="flex:0 0 34px"></span></div>
    <div class="row"><span class="label">LAST NAME</span><span class="fill"></span></div>
    <div class="row"><span class="label">DATE OF BIRTH</span><span class="fill"></span></div>
    <div class="row"><span class="label">ACCOUNT NO</span><span class="fill"></span></div>
  </div>
  <div class="fields" style="left:285px;width:250px">
    <div class="row"><span class="label">ADDRESS</span><span class="fill"></span></div>
    <div class="row"><span class="label">CITY, ZIP CODE</span><span class="fill"></span></div>
    <div class="row"><span class="label">HOME PHONE</span><span class="fill"></span></div>
    <div class="row"><span class="label">MOBILE PHONE</span><span class="fill"></span></div>
  </div>

  <div class="section-bar section-bar--red" style="left:13px;top:227px;width:524px">MEDICAL INFORMATION</div>
  <div class="med-panel">
    <div class="med-row">
      <span>SEX</span><span class="in" style="width:44px;margin-left:10px">F / M</span>
      <span style="margin-left:24px">HEIGHT</span><span class="in" style="width:62px;margin-left:14px"></span>
      <span style="margin-left:28px">WEIGHT</span><span class="in" style="width:62px;margin-left:12px"></span>
      <span style="margin-left:24px">RACE</span><span class="in" style="flex:1;margin-left:13px"></span>
    </div>
    <div class="diag-head"><span>DIAGNOSIS</span><span class="fill"></span></div>
    <ul class="check-col" style="left:13px">
      <li>PCI (no. of stents: ........)</li>
      <li>CABG (no. of vessels: ........)</li>
      <li>MI (last event: ..................)</li>
      <li>PCM/ICD</li>
      <li>Diabetes</li>
    </ul>
    <ul class="check-col" style="left:214px">
      <li>Claustrophobia</li>
      <li>Asthma</li>
      <li>Emphysema</li>
      <li>COPD</li>
      <li>LMP: <span style="display:inline-block;width:84px;border-bottom:1px solid var(--line);margin-left:4px"></span></li>
    </ul>
    <ul class="check-col" style="left:366px">
      <li>bHCG</li>
      <li>Tubal ligation</li>
      <li>Post-menopause &gt; 1 year</li>
      <li>Hysterectomy</li>
    </ul>
  </div>

  <div class="notice"><span class="notice__icon">!</span>Please read the following instructions carefully. You might be rescheduled if any of the following instructions are not met.</div>

  <ul class="instructions">
    <li><b>AVOID caffeine</b> containing products (coffee, tea, soda, chocolate, energy drinks, or some over the counter medications) for 4 hours prior to testing.</li>
    <li><b>AVOID smoking</b> for 4 hours prior to testing.</li>
    <li><b>AVOID eating or drinking</b> anything except water for 4 hours prior to testing.</li>
    <li class="tick">Arrive 15 minutes early for your appointment time.</li>
    <li class="tick">Wear comfortable clothing. Remove any metal objects, such as jewelry or piercings.</li>
    <li class="tick">Women will be asked to remove bras containing metal underwire.</li>
    <li class="tick">Inform your physician or the staff if you are claustrophobic or have a problem staying in restricted environments for any length of time.</li>
    <li class="tick">Inform the physician or the staff if you are or think you might be pregnant</li>
  </ul>

  <p class="ack">I hereby acknowledge that the instructions and procedures pertinent to this study were explained thoroughly,<br>I had time to ask questions, and these questions were addressed satisfactorily.</p>

  <div class="sign" style="left:14px;top:640px">Patient's print name</div>
  <div class="sign" style="left:151px;top:640px">Patient's signature</div>
  <div class="sign" style="left:14px;top:686px">Prescriber's print name</div>
  <div class="sign" style="left:153px;top:686px">Prescriber's signature</div>

  <div class="referral">
    <div class="referral__head">REFERRING PHYSICIAL CONTACT INFORMATION</div>
    <div class="referral__row"><span>ORDER DATE</span></div>
    <div class="referral__row"><span>PHONE NUMBER</span></div>
    <div class="referral__row"><span>FAX NUMBER</span></div>
  </div>

  <div class="foot-bar"></div>
</section>

<!-- INFORMATION SIDE -->
<section class="page page--info" aria-label="Practice information">
  <svg class="header-art" width="555" height="128" viewBox="0 0 555 128">
    <polygon points="178,124 192,124 275,0 261,0" fill="#c81e2d"/>
    <polygon points="204,124 555,124 555,0 287,0" fill="#c81e2d"/>
  </svg>
  <div class="brand" style="left:22px;top:40px;font-size:20px"><span class="brand__dot" style="width:14px;height:14px"></span><span>CRESTFIELD<br>CARDIAC</span></div>
  <div class="title" style="top:28px"><span class="title__top" style="font-size:33px">CALCIUM SCORE</span><span class="title__main" style="font-size:44px;margin-top:2px">HEART SCAN</span></div>

  <div class="photo" role="img" aria-label="Photo of a patient lying on a CT scanner table beside a heart monitor"></div>

  <div class="band band--red" style="top:431px;height:21px;line-height:21px">PHYSICIANS</div>
  <div class="name-strip band--names" style="top:452px;height:27px">
    Dorian Velko, MD<span class="sep">|</span>L.N. Morvesti, MD<span class="sep">|</span>Ovila Brandt, MD<span class="sep">|</span>Tomas Velko, MD<span class="sep">|</span>Gerald Pompetti, MD
  </div>
  <div class="band band--red" style="top:479px;height:22px;line-height:22px">NURSE PRACTITIONERS</div>
  <div class="name-strip" style="top:501px;height:25px;font-size:10px">
    Marla Quenton, MSN, ACNP-BC<span class="sep">|</span>Jessa Alvarro, MSN, APRN, AGNP-C<span class="sep">|</span>Renna Kowalt, MSN, APRN, NP-C
  </div>

  <div class="contact-zone">
    <svg width="555" height="190" viewBox="0 0 555 190" style="position:absolute;left:0;top:0">
      <defs>
        <linearGradient id="mapTone" x1="0" y1="0" x2="1" y2="1">
          <stop offset="0" stop-color="#ecebe6"/>
          <stop offset="1" stop-color="#e2e4e2"/>
        </linearGradient>
      </defs>
      <rect width="555" height="190" fill="url(#mapTone)" role="img" aria-label="Street map showing the practice location"/>
      <polygon points="210,0 555,0 555,146 282,146" fill="#0c0c0c"/>
      <polygon points="282,146 555,146 555,190 310,190" fill="#c81e2d"/>
    </svg>
    <div class="contact-text contact-lead">For appointments or more information on testing:</div>
    <div class="contact-text contact-block">
      <div class="co">Crestfield Cardiac PLLC</div>
      <div class="contact-line" style="margin-left:-15px">
        <svg width="8" height="10" viewBox="0 0 8 10"><path d="M4 0a4 4 0 0 0-4 4c0 3 4 6 4 6s4-3 4-6a4 4 0 0 0-4-4z" fill="#c81e2d"/><circle cx="4" cy="4" r="1.4" fill="#0c0c0c"/></svg>
        <span>712 Harrow Ln. Ste. K</span></div>
      <div>Melrick, TX 77431</div>
      <div class="contact-line" style="margin-left:-15px">
        <svg width="8" height="8" viewBox="0 0 8 8"><path d="M1.5 0l1.6 2-1 1c.6 1.2 1.5 2.1 2.7 2.7l1-1 2 1.6-1 1.7C3.5 8 0 4.5 0 1.2z" fill="#c81e2d"/></svg>
        <span>832-417-2286</span></div>
      <div class="contact-line" style="margin-left:-15px">
        <svg width="9" height="7" viewBox="0 0 9 7"><rect x=".5" y=".5" width="8" height="6" fill="none" stroke="#c81e2d"/><path d="M.5 .5l4 3 4-3" fill="none" stroke="#c81e2d"/></svg>
        <span>832-417-2287</span></div>
    </div>
    <div class="contact-text web">
      <svg width="13" height="13" viewBox="0 0 14 14"><circle cx="7" cy="7" r="6" fill="none" stroke="#fff" stroke-width="1.4"/><ellipse cx="7" cy="7" rx="2.6" ry="6" fill="none" stroke="#fff" stroke-width="1.2"/><path d="M1 7h12" stroke="#fff" stroke-width="1.2"/></svg>
      crestfieldcardiac.example
    </div>
  </div>

  <div class="foot-bar" style="height:9px"></div>
</section>

</body>
</html>
```